Wedding Photo Studio needs custom webpage

I'm changing up my service offering to offer multiple editing styles. I'm looking to update my website to reflect that but still showcase my dreamy edits as an attention grabbing part of the website.

I will have 4 color editing styles (Lucian's Hallmark, Bright & Airy, Velvet Umber, Dreamy) and one black and white style. I have attached sample images in each style.

I also attached a couple dreamy edits that can be used as attention grabbing images.

I'm hoping for some functionality that perhaps takes a single image and divides it by 4 to show 25% in each style that can be clicked on and would 'maximize' the carousel to that style but still have a functionality to go to a different style after being maximized.

You can see www.lucianvphotography-demo.com for the current design and content. It doesn't have to be too different (but can be). It just needs to showcase the multiple editing styles effectively.

Target Market(s)

Couples who are having $20-50k weddings.

Industry/Entity Type

Photography

Coding

Coded - Design and coding required

Number of Pages Required

3 page

Colors

Designer to choose colors to be used in the design.

Requirements
Must have
• Pricing page with toggles for (off-season/on-season, Saturday/non-saturday) accurate pricing, good way to show multiple editing style photos.

```html
<!DOCTYPE html>
<html lang="en">
<head>
<meta charset="utf-8">
<title>Lucian V Photography</title>
<link rel="stylesheet" href="https://fonts.googleapis.com/css2?family=Playfair+Display:wght@700;800&family=Handlee&family=Great+Vibes&display=swap">
<style>
:root{
  --umber:#7a4a14;
  --umber-dark:#5e3810;
  --tan:#cbbd9b;
  --sand:#ddd0b4;
  --cream:#fff;
  --ink:#1f1710;
  --orange:#ef8a25;
}
*{box-sizing:border-box;margin:0;padding:0}
html,body{width:1200px;height:3204px;overflow:hidden}
body{font-family:"Handlee",cursive;color:var(--ink);background:var(--tan)}
.heading{font-family:"Playfair Display",serif;font-weight:800}

/* hero with four-way editing style split */
.hero{position:relative;height:748px;overflow:hidden}
.style-split{position:absolute;inset:0;display:flex}
.style-panel{position:relative;flex:1;border-right:2px solid rgba(255,255,255,.55);
  background:
  radial-gradient(ellipse 360px 165px at 600px 255px,#fff3c4 0%,#ffd07a 30%,rgba(240,150,70,0) 75%),
  linear-gradient(180deg,#6b4a3a 0%,#c7865a 22%,#efb06c 40%,#b9a35a 58%,#7f9a3a 72%,#9aa83a 85%,#6f7a2a 100%);
  background-size:1200px 748px}
.style-panel:last-child{border-right:0}
.style-panel.hallmark{background-position:0 0}
.style-panel.airy{background-position:-300px 0;filter:brightness(1.18) saturate(.75)}
.style-panel.umber{background-position:-600px 0;filter:sepia(.45) saturate(1.2) brightness(.85)}
.style-panel.dreamy{background-position:-900px 0;filter:saturate(1.25) hue-rotate(-12deg) brightness(1.05)}
.style-label{position:absolute;left:50%;bottom:222px;transform:translateX(-50%);white-space:nowrap;
  background:rgba(94,56,16,.78);color:var(--cream);border:1.5px solid rgba(255,255,255,.7);border-radius:18px;
  padding:6px 16px;font-family:"Playfair Display",serif;font-weight:700;font-size:14px}
.style-label.active{background:var(--orange)}
.hero-corner{position:absolute;width:240px;height:260px;background:linear-gradient(135deg,#8b4a1c,#d8b48a);opacity:.85}
.hero-corner.tl{top:0;left:0;border-bottom-right-radius:70%}
.hero-corner.tr{top:0;right:0;border-bottom-left-radius:70%;width:200px}
.hero-corner.bl{bottom:0;left:0;height:160px;border-top-right-radius:80%;background:linear-gradient(45deg,#c8ab84,#ead9bd)}
.hero-corner.br{bottom:0;right:0;height:200px;border-top-left-radius:80%;background:linear-gradient(315deg,#8b4a1c,#e0c7a0)}
.nav{position:absolute;top:0;left:0;right:0;height:52px;display:flex;align-items:center;padding:0 60px 0 120px;background:linear-gradient(180deg,rgba(50,28,12,.75),rgba(50,28,12,0))}
.brand{font-family:"Playfair Display",serif;font-weight:700;color:var(--cream);font-size:26px;display:flex;align-items:center;gap:8px}
.brand-dot{width:10px;height:10px;border-radius:50%;background:var(--cream)}
.nav-links{display:flex;gap:34px;margin-left:auto;list-style:none}
.nav-links li{font-family:"Playfair Display",serif;font-weight:700;font-size:15px;color:var(--cream)}
.pill-outline{margin-left:36px;border:1.5px solid var(--cream);color:var(--cream);border-radius:20px;padding:7px 18px;font-family:"Playfair Display",serif;font-weight:700;font-size:15px}

/* about */
.about{height:696px;background:var(--tan);position:relative}
.about-photo{position:absolute;left:92px;top:64px;width:460px;height:500px;transform:rotate(-4deg);border:4px solid #c9a24a;background:linear-gradient(135deg,#5f7a3a,#a9b98a 40%,#e9d6c1 70%,#b98f70)}
.about-text{position:absolute;left:600px;top:236px;width:540px}
.about-text h2{font-size:38px;text-align:center;margin-bottom:24px}
.about-text p{font-size:14px;line-height:1.55}
.signature{font-family:"Great Vibes",cursive;font-size:30px;margin:22px 0 0 160px}

/* testimonials */
.testimonials{height:488px;background:var(--sand);position:relative;text-align:center}
.testimonials h2{font-size:38px;padding-top:66px}
.quote{width:1040px;margin:28px auto 0;font-size:15px;line-height:1.5;font-style:italic}
.reviewer{display:flex;justify-content:center;align-items:center;gap:16px;margin-top:30px}
.avatar{width:80px;height:80px;border-radius:50%;background:linear-gradient(135deg,#b63b4a,#f0c7b8)}
.reviewer-name{font-family:"Playfair Display",serif;font-weight:700;font-size:17px}
.arrow{position:absolute;top:230px;width:26px;height:26px}
.arrow.prev{left:56px}.arrow.next{right:56px}
.dots{display:flex;justify-content:center;gap:10px;margin-top:44px}
.dots span{width:11px;height:11px;border-radius:50%;background:#fff}
.dots span.on{background:#444}

/* availability + pricing toggles */
.availability{height:240px;background:var(--umber);padding:30px 60px 0}
.avail-form{border:1.5px solid rgba(255,255,255,.7);border-radius:60px;height:120px;display:flex;align-items:center;gap:18px;padding:0 24px}
.field{display:flex;flex-direction:column;gap:8px}
.field label{font-family:"Playfair Display",serif;font-weight:700;color:var(--cream);font-size:13px}
.field .input{width:190px;height:40px;border-radius:20px;background:#fff;color:#999;font-size:13px;padding:11px 18px}
.btn-cta{margin-top:22px;height:42px;border-radius:21px;background:var(--orange);color:#fff;font-family:"Playfair Display",serif;font-weight:700;font-size:14px;padding:12px 18px;white-space:nowrap}
.pricing-toggles{display:flex;justify-content:center;align-items:center;gap:40px;margin-top:22px;color:var(--cream);font-size:14px}
.toggle{display:flex;align-items:center;gap:10px}
.switch{width:40px;height:20px;border-radius:10px;background:var(--orange);position:relative}
.switch::after{content:"";position:absolute;top:3px;left:3px;width:14px;height:14px;border-radius:50%;background:#fff}
.switch.on::after{left:23px}
.price{font-family:"Playfair Display",serif;font-weight:700;font-size:15px}

/* portfolio */
.portfolio{height:628px;background:var(--tan);text-align:center;position:relative}
.portfolio h2{font-size:38px;padding-top:66px}
.portfolio .sub{font-size:14px;margin-top:8px;font-style:italic}
.cards{position:absolute;top:176px;left:88px;right:48px;display:flex;gap:16px}
.card{display:flex;flex-direction:column;align-items:center}
.card .media{border-radius:18px;height:304px}
.card.photos .media{width:504px;background:linear-gradient(160deg,#3b4a2e,#6f7f4a 45%,#d8d3c8 75%,#8a8376)}
.card.videos .media{width:544px;background:linear-gradient(180deg,#0e1a3a,#2b3f7a 40%,#d57a3a 62%,#3a2a20)}
.pill-umber{margin-top:34px;background:var(--umber);color:#fff;border:1.5px solid rgba(255,255,255,.6);border-radius:20px;padding:8px 26px;font-family:"Playfair Display",serif;font-weight:700;font-size:14px}

/* footer */
.footer{height:404px;background:var(--umber);color:var(--cream);text-align:center;padding-top:60px}
.footer .brand{justify-content:center;font-size:34px}
.footer-nav{display:flex;justify-content:center;gap:30px;list-style:none;margin-top:26px}
.footer-nav li{font-family:"Playfair Display",serif;font-weight:700;font-size:15px}
.contact{display:flex;justify-content:center;gap:30px;margin-top:18px;font-size:13px}
.contact span{display:flex;align-items:center;gap:6px}
.social{display:flex;justify-content:center;gap:20px;margin-top:26px}
.social span{width:20px;height:20px;border-radius:50%;border:2px solid var(--cream)}
.copyright{font-size:12px;margin-top:26px}
</style>
</head>
<body>
<header class="hero">
  <div class="style-split" role="img" aria-label="Couple embracing in a golden meadow at sunset, shown in four editing styles">
    <div class="style-panel hallmark"><span class="style-label active">Lucian's Hallmark</span></div>
    <div class="style-panel airy"><span class="style-label">Bright &amp; Airy</span></div>
    <div class="style-panel umber"><span class="style-label">Velvet Umber</span></div>
    <div class="style-panel dreamy"><span class="style-label">Dreamy</span></div>
  </div>
  <div class="hero-corner tl" role="img" aria-label="Floral corner decoration"></div>
  <div class="hero-corner tr" role="img" aria-label="Floral corner decoration"></div>
  <div class="hero-corner bl" role="img" aria-label="Floral corner decoration"></div>
  <div class="hero-corner br" role="img" aria-label="Floral corner decoration"></div>
  <nav class="nav">
    <div class="brand"><span class="brand-dot"></span>Lucian V</div>
    <ul class="nav-links"><li>Home</li><li>The Team</li><li>Portfolio ▾</li><li>Blog</li><li>Pricing</li><li>Contact Me</li></ul>
    <div class="pill-outline">Check Availability ⓘ</div>
  </nav>
</header>

<section class="about">
  <div class="about-photo" role="img" aria-label="Photographer holding a baby, framed with flowers"></div>
  <div class="about-text">
    <h2 class="heading">About Me</h2>
    <p>I am an accountant by day, photographer by night. I never had a happy life until I found my true calling: telling stories through a lens. Wedding photography is now the part of life I love most. I serve couples across the region and will travel anywhere the day takes me. If you feel that spark too, please reach out. I would be happy to meet with you and hear about your big day.</p>
    <div class="signature">Lucian Vance</div>
  </div>
</section>

<section class="testimonials">
  <h2 class="heading">Testimonials</h2>
  <p class="quote">Lucian is the absolute best! He did a SPECTACULAR job with our wedding photos. He got images of everything, even the things that we never thought he would notice. Hands down the best photographer I have seen in the area, and you will not be disappointed!</p>
  <div class="reviewer"><div class="avatar" role="img" aria-label="Couple portrait"></div><div class="reviewer-name">Nora &amp; Jules</div></div>
  <div class="dots"><span class="on"></span><span></span><span></span><span></span></div>
  <svg class="arrow prev" viewBox="0 0 24 24"><path d="M16 3 7 12l9 9" fill="none" stroke="#1f1710" stroke-width="3"/></svg>
  <svg class="arrow next" viewBox="0 0 24 24"><path d="m8 3 9 9-9 9" fill="none" stroke="#1f1710" stroke-width="3"/></svg>
</section>

<section class="availability">
  <div class="avail-form">
    <div class="field"><label>Name</label><div class="input">Name</div></div>
    <div class="field"><label>Email</label><div class="input">Email</div></div>
    <div class="field"><label>Phone</label><div class="input">Phone</div></div>
    <div class="field"><label>Event Date</label><div class="input">mm/dd/yyyy</div></div>
    <div class="btn-cta">Check Availability ⓘ</div>
  </div>
  <div class="pricing-toggles">
    <div class="toggle">Off-Season <span class="switch on"></span> On-Season</div>
    <div class="toggle">Non-Saturday <span class="switch"></span> Saturday</div>
    <div class="price">Packages from $3,400</div>
  </div>
</section>

<section class="portfolio">
  <h2 class="heading">Portfolio</h2>
  <p class="sub">Check our memorable works through Photos and Videos!</p>
  <div class="cards">
    <div class="card photos"><div class="media" role="img" aria-label="Bride and groom walking hand in hand outdoors"></div><div class="pill-umber">Photos ⓘ</div></div>
    <div class="card videos"><div class="media" role="img" aria-label="Couple outside a lit venue at night"></div><div class="pill-umber">Videos ⓘ</div></div>
  </div>
</section>

<footer class="footer">
  <div class="brand"><span class="brand-dot"></span>Lucian V</div>
  <ul class="footer-nav"><li>Home</li><li>The Team</li><li>Portfolio ▾</li><li>Blog</li><li>Pricing</li><li>Contact Me</li></ul>
  <div class="contact">
    <span><svg width="14" height="12" viewBox="0 0 14 12"><rect x="1" y="1" width="12" height="10" fill="none" stroke="#fff" stroke-width="1.5"/><path d="m1 1 6 5 6-5" fill="none" stroke="#fff" stroke-width="1.5"/></svg>hello@lucianvphotography-demo.com</span>
    <span><svg width="12" height="12" viewBox="0 0 24 24"><path d="M6 2h4l2 5-3 2a11 11 0 0 0 6 6l2-3 5 2v4a2 2 0 0 1-2 2A18 18 0 0 1 4 4a2 2 0 0 1 2-2z" fill="#fff"/></svg>555-014-2290</span>
  </div>
  <div class="social"><span></span><span></span></div>
  <p class="copyright">Copyright © 2024 lucianvphotography. Powered by lucianvphotography</p>
</footer>
</body>
</html>
```